Website Design for Non-profit

We are looking for a new site design for the Patrons of the Northvale Heritage Hall. The current site can be found at
http://www.patrons-nhh.org/nhhindex_e.html
The URL is provided for reference. We want a completely different look and layout which is shown in the specifications document. Visiting the site, you can learn more about the organization.
Initially, we would like a home page, and inside page provided. Once we a home page and inside page are selected, we would like a simple mobile template provided.
I have attached a full description of the project as well as the specifications document and a zip file containing images for the site.
As mentioned in the specs document, we want to include an image of the museum in the header. The zip file is too large for us to upload (80 meg). The zip file can be obtained by clicking this link:
http://qzl.cc/TrVkWp
The zip file contains several exterior photos and you can select the one you feel is most appropriate to your design.
Updates
Project Deadline Extended
Reason: A long weekend is coming up and a few members of the team are unavailable for review.
Project Deadline Extended
Reason: Reviewing designs. Should have a decision next week.
Project Deadline Extended
Reason: We are discussing the designs and looking to reach a consensus. I will be implementing some designs today or tomorrow. Hopefully final selection will be next week.
Project Deadline Extended
Reason: Still reviewing designs. Hope to get a decision soon.
Project Deadline Extended
Reason: Working to finalize the design. Very close.
Project Deadline Extended
Industry/Entity Type
Museum
Look and feel

```html
<!DOCTYPE html>
<html lang="en">
<head>
<meta charset="utf-8">
<title>Patrons of the Northvale Heritage Hall</title>
<link href="https://fonts.googleapis.com/css2?family=Roboto:wght@400;500&display=swap" rel="stylesheet">
<style>
:root{
  --red:#c1272d;
  --red-dark:#9e1c22;
  --blue:#1ea7d8;
  --blue-dark:#168bb6;
  --gold:#a48f3b;
  --bar:#2d2d2d;
  --text:#555;
  --muted:#777;
  --line:#dcdcdc;
  --white:#fff;
}
*{box-sizing:border-box;margin:0;padding:0}
html,body{width:1152px;height:1200px;overflow:hidden;background:var(--white);font-family:"Roboto",Arial,sans-serif;color:var(--text)}
.page{position:relative;width:1152px;height:1200px}
.abs{position:absolute}

/* top bar */
.topbar{left:0;top:0;width:1152px;height:30px;background:var(--bar)}
.social{top:4px;width:22px;height:22px;border-radius:2px}
.social.one{left:116px;background:#3b5b99}
.social.two{left:145px;background:#c4302b}
.toplinks{left:200px;top:0;height:30px;display:flex;align-items:center;gap:30px;font-size:11px;color:#bbb;letter-spacing:.3px}
.toplinks small{font-size:7px}
.sizer{left:786px;top:0;height:30px;display:flex;align-items:center;gap:14px;font-size:12px;color:#fff;font-weight:500}
.search{left:874px;top:4px;width:163px;height:22px;background:#fff;border-radius:2px}
.search svg{position:absolute;right:8px;top:6px}

/* brand */
.brand{left:115px;top:62px;display:flex;align-items:center;gap:12px}
.brand-mark{width:34px;height:34px;background:var(--blue)}
.brand-name{font-size:22px;font-weight:500;color:var(--gold);line-height:1.15;width:300px}

/* hero */
.hero{left:115px;top:151px;width:922px;height:341px;background:linear-gradient(100deg,#7a5a2e 0%,#b68a3e 30%,#556a58 55%,#8a7c3a 80%,#b4a466 100%)}
.dots{left:525px;top:458px;display:flex;gap:8px}
.dots span{width:9px;height:9px;border-radius:50%;background:#222;border:1px solid #555}
.dots span.on{background:#e36a2a;border:2px solid #fff}

.nav{left:115px;top:492px;width:922px;height:48px;background:linear-gradient(#c8282e,#b42026);display:flex;align-items:center;justify-content:space-between;padding:0 10px;color:#fff;font-size:14px;font-weight:500;box-shadow:0 2px 3px rgba(0,0,0,.2)}

/* tabs */
.tabs{left:115px;top:559px;display:flex;gap:12px}
.tab{height:32px;padding:0 13px;display:flex;align-items:center;font-size:14px;color:#fff;background:var(--blue);border:1px solid var(--blue-dark)}
.tab.active{background:#fff;color:#555;border:1px solid var(--line);border-bottom-color:#fff;height:33px}
.intro{left:115px;top:591px;width:922px;height:158px;border:1px solid var(--line);border-radius:0 0 3px 3px;padding:16px 9px;font-size:11.1px;line-height:18px;box-shadow:0 1px 2px rgba(0,0,0,.08)}
.intro p+p{margin-top:18px}

/* left column */
.btn{left:115px;width:190px;height:43px;display:flex;align-items:center;gap:12px;padding-left:8px;color:#fff;font-weight:500;background:linear-gradient(#27b3e3,#168fbf);border:1px solid var(--blue-dark)}
.btn .ico{width:30px;height:28px}
.btn.vol{top:765px;font-size:12.5px}
.btn.don{top:818px;font-size:13.5px}
.bureau{left:115px;top:871px;width:190px;height:205px;border:1px solid var(--line);overflow:hidden}
.bureau h3{height:37px;background:linear-gradient(#b09a45,#948134);color:#fff;font-size:13.5px;font-weight:500;display:flex;align-items:center;padding-left:9px}
.bureau .body{padding:8px 4px;font-size:11.2px;line-height:16.5px;text-align:justify;hyphens:auto;-webkit-hyphens:auto}
.bureau .body p+p{margin-top:16px}
.bureau a{color:var(--blue);text-decoration:none;display:block;margin-top:2px}

/* news */
.panel{left:317px;width:478px;height:148px;border:1px solid var(--line);overflow:hidden}
.panel.events{top:765px}
.panel.news{top:928px}
.panel-head{height:42px;border-bottom:1px solid var(--line);display:flex;align-items:center;justify-content:space-between;padding:0 7px 0 9px;font-size:13.5px;color:#444}
.panel-head .more{color:var(--red);font-size:12px;font-weight:500}
.item{display:flex;gap:12px;padding:8px 7px}
.thumb{width:83px;height:83px;flex:none;margin-top:1px}
.thumb.sea{background:linear-gradient(#9cc0dc 0%,#b7cde0 38%,#2c4a6a 45%,#1a2e46 100%)}
.thumb.sky{background:linear-gradient(#3d7fa6,#8bb7cc 60%,#6f8a74)}
.item h4{font-size:12px;font-weight:400;color:var(--red);line-height:16px;white-space:nowrap}
.item .date{font-size:11px;line-height:19px;color:#666}
.item p{font-size:10.6px;line-height:18.3px;text-align:justify;color:#666;hyphens:auto;-webkit-hyphens:auto}

/* feature tiles */
.tile{left:807px;width:229px;height:147px;border:1px solid var(--line);padding:1px}
.tile.gal{top:766px}
.tile.mem{top:929px}
.tile .img{width:100%;height:100%;background:linear-gradient(135deg,#3b3a2e,#6f6f4e 45%,#8a8c6a 70%,#4b4a3c)}
.tile .label{position:absolute;left:1px;bottom:22px;height:38px;width:142px;background:var(--red);color:#fff;font-size:13.5px;font-weight:500;display:flex;align-items:center;padding-left:11px;clip-path:polygon(0 0,91% 0,100% 100%,0 100%)}
.tile.mem .label{width:170px;bottom:17px}

/* footer */
.rule{left:115px;top:1094px;width:922px;height:1px;background:#e6e6e6}
.flinks{left:115px;top:1124px;display:flex;gap:19px;font-size:11px;color:#666}
.badge{top:1108px;height:44px}
.badge.a{left:733px;width:52px;background:#f3e2e0}
.badge.b{left:795px;width:58px;background:#f3e2e0}
.badge.c{left:868px;width:168px;height:34px;top:1113px;background:#e3eef3}
.bottombar{left:0;top:1166px;width:1152px;height:34px;background:var(--bar);color:#e6e6e6;font-size:12px;display:flex;align-items:center;justify-content:space-between;padding:0 115px 0 116px}
</style>
</head>
<body>
<div class="page">
  <div class="abs topbar"></div>
  <div class="abs social one"></div>
  <div class="abs social two"></div>
  <nav class="abs toplinks">
    <span>CONTACT</span><span>RELATED SITES</span><span>DONATE</span><span>SITEMAP</span><span>FRANÇAIS</span><span>MEMBER LOGIN <small>(NOT A MEMBER?)</small></span>
  </nav>
  <div class="abs sizer"><span>A-</span><span>A</span><span>A+</span></div>
  <div class="abs search"><svg width="9" height="9" viewBox="0 0 9 9"><circle cx="3.5" cy="3.5" r="2.5" fill="none" stroke="#666" stroke-width="1.2"/><line x1="5.5" y1="5.5" x2="8.5" y2="8.5" stroke="#666" stroke-width="1.2"/></svg></div>

  <div class="abs brand">
    <div class="brand-mark"></div>
    <div class="brand-name">Patrons of the Northvale Heritage Hall</div>
  </div>

  <div class="abs hero" role="img" aria-label="Photograph of a veteran guiding visitors through a museum exhibit"></div>
  <div class="abs dots"><span></span><span class="on"></span><span></span><span></span></div>

  <nav class="abs nav">
    <span>HOME</span><span>ABOUT</span><span>SUPPORT PNHH</span><span>EVENTS</span><span>PROJECTS &amp; PROGRAMS</span><span>MEET THE PATRONS</span><span>VOLUNTEERS</span><span>PUBLICATIONS</span>
  </nav>

  <div class="abs tabs">
    <div class="tab active">BE A PATRON</div>
    <div class="tab">BE A DONOR</div>
    <div class="tab">BE A VOLUNTEER</div>
  </div>
  <div class="abs intro">
    <p>Lorem ipsum dolor sit amet, consectetur adipisicing elit, sed do eiusmod tempor incididunt ut labore et dolore magna aliqua. Ut enim ad minim veniam, quis nostrud exercitation ullamco laboris nisi ut aliquip ex ea commodo consequat. Duis aute irure dolor in reprehenderit in voluptate velit esse cillum dolore eu fugiat nulla pariatur. Excepteur sint occaecat cupidatat non proident, sunt in culpa qui officia deserunt mollit anim id est laborum</p>
    <p>Lorem ipsum dolor sit amet, consectetur adipisicing elit, sed do eiusmod tempor incididunt ut labore et dolore magna aliqua. Ut enim ad minim veniam, quis nostrud exercitation ullamco laboris nisi ut aliquip ex ea commodo consequat. Duis aute irure dolor in reprehenderit in voluptate velit esse cillum dolore eu fugiat nulla pariatur. Excepteur sint occaecat cupidatat non proident, sunt in culpa qui officia deserunt mollit anim id est laborum</p>
  </div>

  <div class="abs btn vol">
    <svg class="ico" viewBox="0 0 30 28"><circle cx="10" cy="8" r="5" fill="#f1c27d"/><rect x="3" y="15" width="14" height="12" rx="5" fill="#2f6fb0"/><circle cx="21" cy="11" r="4.5" fill="#f1c27d"/><rect x="14" y="17" width="14" height="10" rx="4" fill="#e98a2b"/></svg>
    <span>BECOME A VOLUNTEER</span>
  </div>
  <div class="abs btn don">
    <svg class="ico" viewBox="0 0 30 28"><path d="M13 24 L3 13 A6 6 0 0 1 13 6 A6 6 0 0 1 23 13 Z" fill="#f08080"/><rect x="12" y="15" width="15" height="10" rx="1" fill="#8cc152"/></svg>
    <span>DONATE NOW</span>
  </div>
  <aside class="abs bureau">
    <h3>SPEAKER'S BUREAU</h3>
    <div class="body">
      <p>Lorem ipsum dolor sit amet, consectetur adipisicing elit, sed do eiusmod tempor incididunt ut labore et dolore magna aliqua.</p>
      <p>Ut enim ad minim veniam, quis nostrud exercitation ullamco laboris nisi ut aliquip</p>
      <a href="#">Read More</a>
    </div>
  </aside>

  <section class="abs panel events">
    <div class="panel-head"><span>LATEST EVENTS</span><span class="more">MORE</span></div>
    <div class="item">
      <div class="thumb sea" role="img" aria-label="Photo of a submarine at sea"></div>
      <div>
        <h4>Lorem ipsum dolor sit amet, consectetur adipisicing elit,</h4>
        <div class="date">July 30,2013</div>
        <p>Ut enim ad minim veniam, quis nostrud exercitation ullamco laboris nisi ut aliquip ex ea commodo consequat. Duis aute irure dolor in reprehenderit in voluptate velit esse cillum dolore eu fugiat nulla pariatur.</p>
      </div>
    </div>
  </section>
  <section class="abs panel news">
    <div class="panel-head"><span>ANNOUNCEMENTS</span><span class="more">MORE</span></div>
    <div class="item">
      <div class="thumb sky" role="img" aria-label="Photo of a vintage aircraft in flight"></div>
      <div>
        <h4>Lorem ipsum dolor sit amet, consectetur adipisicing elit,</h4>
        <div class="date">July 30,2013</div>
        <p>Ut enim ad minim veniam, quis nostrud exercitation ullamco laboris nisi ut aliquip ex ea commodo consequat. Duis aute irure dolor in reprehenderit in voluptate velit esse cillum dolore eu fugiat nulla pariatur.</p>
      </div>
    </div>
  </section>

  <div class="abs tile gal">
    <div class="img" role="img" aria-label="Photo of a gallery hall with a tank on display"></div>
    <div class="label">PHOTO GALLERY</div>
  </div>
  <div class="abs tile mem">
    <div class="img" role="img" aria-label="Photo of member artefacts on display in the hall"></div>
    <div class="label">MEMBER TREASURES</div>
  </div>

  <div class="abs rule"></div>
  <nav class="abs flinks">
    <span>Home</span><span>About</span><span>Support PNHH</span><span>Events</span><span>Projects &amp; Programs</span><span>Meet the Patrons</span><span>Volunteers</span><span>Publications</span>
  </nav>
  <div class="abs badge a"></div>
  <div class="abs badge b"></div>
  <div class="abs badge c"></div>

  <footer class="abs bottombar">
    <span>Copyright 2013 Patrons of the Northvale Heritage Hall. All Rights Reserved.</span>
    <span>12 Harbour Lane, Northvale, Ontario N0V 2H4</span>
  </footer>
</div>
</body>
</html>
```